I am looking for a poster design with a pledge for my clients to take. The pledge will be to not use tanning beds. Our company is a Spray Tanning Salon that focuses on educating our clients on the dangers of indoor tanning while offering a safe alternative through spray tanning. I have an outline of a possible wording but I am VERY open to adjustments on it!
This is not a promotional poster. This is a poster that will be hanging in the salon and our clients will sign around the wall.
Updates

Project Deadline Extended Reason: Not currently in love with any submissions and would like to see more. Looking for a more simple design overall. Added Friday, October 28, 2016

Target Market(s)

Women 20-30 years old

Industry/Entity Type

Salon

Font styles to use
Sans Serif

Requirements
Must have
• Take the pledge to ditch the bed!
• Willowmere Tanning
• **Overall simple design, yet eye catching is requested. Not so busy**
Nice to have
• I am open to different wording!
• I pledge to be timeless
• -UVA rays in tanning beds cause wrinkles and other signs of premature aging
• I pledge to be fearless
• -Using tanning beds can cause severe eye damage, a weakened immune system, and melanoma the deadliest form of skin cancer.
• I pledge to be Sunless!
• -Join the LumaVeil revolution at Willowmere Tanning, Grand Rapids first Sunless Spa Experience.
Should not have
• The photo of the salon on it. I included that photo simply for reference of design, this is where this poster will be hung.

```html
<!DOCTYPE html>
<html lang="en">
<head>
<meta charset="utf-8">
<title>Pledge Poster – Willowmere Tanning</title>
<link rel="stylesheet" href="https://fonts.googleapis.com/css2?family=Overpass+Mono:wght@300;400&family=Quicksand:wght@400;500&display=swap">
<style>
  :root {
    --paper: #ffffff;
    --blush: #f2bcbd;
    --ink: #6e6264;
    --script: #ffffff;
    --olive: #cfc452;
    --rose-shadow: #d592b4;
    --lilac: #b9a3d6;
    --leaf: #9cbf62;
    --magenta: #e5529b;
    --sky: #8fcfe0;
    --butter: #f2d46a;
    --coral: #ee8a78;
    --amber: #efa232;
    --logo: #4a4a4a;
  }
  * { box-sizing: border-box; margin: 0; padding: 0; }
  html, body { width: 846px; height: 1200px; overflow: hidden; background: var(--paper); }
  .poster { position: relative; width: 846px; height: 1200px; background: var(--paper); overflow: hidden; }
  .poster-art { position: absolute; inset: 0; }
  .pledge-text { position: absolute; inset: 0; text-align: center; color: var(--ink); }
  .headline {
    position: absolute; left: 0; top: 40px; width: 846px;
    font-family: "Quicksand", sans-serif; font-weight: 500;
    font-size: 30px; letter-spacing: 2px; line-height: 1;
    color: var(--ink); white-space: nowrap;
  }
  .lead-in, .fact {
    position: absolute; left: 0; width: 846px; white-space: nowrap;
    font-family: "Overpass Mono", monospace; font-weight: 300; font-style: italic;
  }
  .lead-in { font-size: 17px; letter-spacing: 1.5px; line-height: 1; }
  .fact--timeless { top: 270px; font-size: 19px; letter-spacing: 1.6px; line-height: 26px; }
  .fact--fearless { top: 636px; font-size: 15px; letter-spacing: 1.3px; line-height: 23px; }
  .fact--sunless { top: 968px; font-size: 19px; letter-spacing: 1.9px; line-height: 30px; }
  .pledge-word {
    position: absolute; left: 0; width: 846px;
    font-family: "Quicksand", sans-serif; font-weight: 400;
    color: var(--script); font-size: 92px; line-height: 1; letter-spacing: 1px;
  }
  .brand {
    position: absolute; left: 0; top: 1096px; width: 846px;
    font-family: "Overpass Mono", monospace; font-weight: 400; font-size: 22px;
    color: var(--logo); text-align: center; letter-spacing: 1px; white-space: nowrap;
  }
</style>
</head>
<body>
<main class="poster">
  <svg class="poster-art" width="846" height="1200" viewBox="0 0 846 1200">
    <rect class="backdrop-panel" x="78" y="124" width="692" height="952" fill="var(--blush)"/>

    <g class="pattern-triangles">
      <polygon role="img" aria-label="Hatched lilac triangle pattern" points="136,104 44,266 232,266" fill="var(--lilac)" opacity="0.7"/>
      <polygon role="img" aria-label="Dotted green and magenta triangle pattern" points="588,88 812,88 700,264" fill="var(--leaf)" opacity="0.6"/>
      <polygon role="img" aria-label="Hatched sky blue triangle pattern" points="732,316 668,428 792,428" fill="var(--sky)" opacity="0.6"/>
      <polygon role="img" aria-label="Hatched yellow triangle pattern" points="552,424 704,424 628,552" fill="var(--butter)" opacity="0.6"/>
      <polygon role="img" aria-label="Dashed pink triangle pattern" points="40,500 196,416 196,600" fill="var(--magenta)" opacity="0.35"/>
      <polygon role="img" aria-label="Dotted coral triangle pattern" points="268,664 268,860 400,740" fill="var(--coral)" opacity="0.5"/>
      <polygon role="img" aria-label="Dashed orange triangle pattern" points="680,680 572,864 800,864" fill="var(--amber)" opacity="0.55"/>
      <polygon role="img" aria-label="Dotted magenta and yellow triangle pattern" points="164,948 48,1120 272,1120" fill="var(--magenta)" opacity="0.55"/>
    </g>

    <g class="hourglass">
      <polygon points="276,328 560,328 432,588" fill="var(--rose-shadow)" opacity="0.85"/>
      <polygon points="432,588 284,792 560,792" fill="var(--rose-shadow)" opacity="0.85"/>
      <polygon points="296,340 572,340 436,576" fill="var(--olive)"/>
      <polygon points="436,576 304,788 584,788" fill="var(--olive)"/>
    </g>

    <g class="word-swashes" fill="none" stroke="var(--script)" stroke-width="3" stroke-linecap="round">
      <path d="M150,240 C190,228 215,246 240,238"/>
      <path d="M606,222 C630,196 660,190 690,196"/>
      <path d="M150,574 C190,584 215,570 238,560"/>
      <path d="M608,548 C640,542 670,560 700,578"/>
      <path d="M160,910 C200,918 225,906 250,896"/>
      <path d="M596,892 C630,872 660,892 686,914"/>
    </g>
  </svg>

  <section class="pledge-text">
    <h1 class="headline">Take the pledge to ditch the bed!</h1>

    <p class="lead-in" style="top:130px">I pledge to be</p>
    <h2 class="pledge-word" style="top:158px">timeless</h2>
    <p class="fact fact--timeless">UVA rays in tanning beds cause wrinkles and other<br>signs of premature aging</p>

    <p class="lead-in" style="top:466px">I pledge to be</p>
    <h2 class="pledge-word" style="top:496px">fearless</h2>
    <p class="fact fact--fearless">Using tanning beds can cause severe eye damage, a weakened immune<br>system and melanoma (the deadliest form of skin cancer)</p>

    <p class="lead-in" style="top:810px">I pledge to be</p>
    <h2 class="pledge-word" style="top:846px">sunless</h2>
    <p class="fact fact--sunless">Join the LumaVeil revolution at Willowmere Tanning;<br>Grand Rapids’ first sunless spa experience!</p>
  </section>

  <p class="brand">Willowmere Tanning</p>
</main>
</body>
</html>
```